Orva Business Card

we need a business card for flooring business called Orva Flooring, the design should be black and white. we have 2 locations

Harwick Showroom
527 Kellerman Road,
Harwick VIC 3148

Elmsworth Showroom
462 Bramwell Hwy,
Elmsworth VIC 3206

email : sales@orvaflooring.com.au
(03) 9471 2830

Please inform we sell , Laminate, Hybrid, Timber, carpet and commercial flooring

```html
<!DOCTYPE html>
<html lang="en">
<head>
<meta charset="utf-8">
<title>Orva Flooring – Business Card</title>
<link rel="stylesheet" href="https://fonts.googleapis.com/css2?family=Roboto:wght@300;400;700&display=swap">
<style>
  :root {
    --ink: #0b0b0b;
    --paper: #ffffff;
    --backdrop: #e9e7e4;
    --rule: #1a1a1a;
  }
  * { box-sizing: border-box; margin: 0; padding: 0; }
  html, body {
    width: 1200px; height: 1200px; overflow: hidden;
    background: var(--backdrop);
    font-family: "Roboto", Arial, sans-serif;
  }
  .canvas {
    width: 1200px; height: 1200px;
    display: flex; flex-direction: column; align-items: center;
    justify-content: center; gap: 26px;
  }
  .card {
    width: 880px; height: 538px; position: relative; overflow: hidden;
    box-shadow: 0 10px 30px rgba(0,0,0,.18);
  }

  /* Front */
  .card--front { background: var(--ink); color: var(--paper); }
  .brand {
    font-weight: 300; text-transform: uppercase; line-height: 1.05;
    letter-spacing: .08em;
  }
  .card--front .brand {
    position: absolute; left: 0; right: 0; top: 150px; text-align: center;
    font-size: 58px; color: var(--paper);
  }
  .services {
    position: absolute; left: 0; right: 0; top: 372px; text-align: center;
    font-weight: 700; font-size: 25px; letter-spacing: .01em;
  }

  /* Back */
  .card--back { background: var(--paper); color: var(--ink); }
  .card--back .brand {
    position: absolute; left: 70px; top: 190px;
    font-size: 52px; color: var(--ink);
  }
  .contact {
    position: absolute; left: 470px; top: 52px; width: 380px;
    font-weight: 400; font-size: 25px; line-height: 1.22;
  }
  .contact-row { display: flex; align-items: flex-start; gap: 18px; }
  .contact-row svg { flex: none; margin-top: 4px; }
  .contact-phone { font-size: 31px; align-items: center; }
  .contact-phone svg { margin-top: 0; }
  .divider { height: 2px; background: var(--rule); margin: 20px 0 20px 60px; width: 280px; }
  .address { text-align: center; }
  .email-band {
    position: absolute; left: 0; bottom: 0; width: 590px; height: 82px;
    background: var(--ink);
    clip-path: polygon(0 0, 520px 0, 590px 100%, 0 100%);
    display: flex; align-items: center; padding-left: 60px;
  }
  .email { color: var(--paper); font-weight: 700; font-size: 30px; }
</style>
</head>
<body>
<main class="canvas">
  <section class="card card--front" aria-label="Card front">
    <div class="brand">Orva<br>Flooring</div>
    <p class="services">Laminate • Hybrid • Timber • Carpet • Commercial flooring</p>
  </section>

  <section class="card card--back" aria-label="Card back">
    <div class="brand">Orva<br>Flooring</div>

    <div class="contact">
      <div class="contact-row contact-phone">
        <svg width="34" height="34" viewBox="0 0 34 34" aria-hidden="true">
          <circle cx="17" cy="17" r="15" fill="none" stroke="currentColor" stroke-width="2.4"/>
          <path d="M11.5 10.5c1-.8 2-.6 2.6.3l1.4 2.2c.5.8.3 1.6-.4 2.1l-1 .7c.8 1.9 2.2 3.3 4.1 4.1l.7-1c.5-.7 1.3-.9 2.1-.4l2.2 1.4c.9.6 1.1 1.6.3 2.6-1.2 1.5-3 1.9-4.8 1.1-3.6-1.6-6.2-4.200-7.8-7.8-.8-1.8-.4-3.6 1.1-4.8z" fill="currentColor"/>
        </svg>
        <span>(03) 9471 2830</span>
      </div>
      <div class="divider"></div>
      <div class="contact-row">
        <svg width="24" height="34" viewBox="0 0 24 34" aria-hidden="true">
          <path d="M12 1C5.9 1 1 5.9 1 12c0 8 11 21 11 21s11-13 11-21C23 5.9 18.1 1 12 1z" fill="currentColor"/>
          <circle cx="12" cy="12" r="4.2" fill="#fff"/>
        </svg>
        <p class="address">Harwick Showroom<br>527 Kellerman Road,<br>Harwick VIC 3148</p>
      </div>
      <div class="divider"></div>
      <div class="contact-row">
        <svg width="24" height="34" viewBox="0 0 24 34" aria-hidden="true">
          <path d="M12 1C5.9 1 1 5.9 1 12c0 8 11 21 11 21s11-13 11-21C23 5.9 18.1 1 12 1z" fill="currentColor"/>
          <circle cx="12" cy="12" r="4.2" fill="#fff"/>
        </svg>
        <p class="address">Elmsworth Showroom<br>462 Bramwell Hwy,<br>Elmsworth VIC 3206</p>
      </div>
    </div>

    <div class="email-band">
      <span class="email">sales@orvaflooring.com.au</span>
    </div>
  </section>
</main>
</body>
</html>
```